Business Card Design Project

Business card design based on the existing logo.

Target Market(s)

Small to medium business owners and CIO's looking for professional IT services.

Industry/Entity Type

Business

Font styles to use
Serif
Sans Serif

Requirements
Must have
• Logo, company name, company details

Text to appear on the business card
Name / Title:
Leon Fairholt
CEO

Address:
Valtiro Limited
Level 3, 42 Kestle St
P O Box 462
Paraparaumu 5391

Other details:
leon@valtiro.co
Ph: 0800 519 308
Mob: +64 21 948 216
www.valtiro.co

Nice to have
• I would look at both single and double sided options. My initial thought is double sided with just the logo with the grey framing for the front and the name and details on the back. But I'm open to other design options.

```html
<!DOCTYPE html>
<html lang="en">
<head>
<meta charset="utf-8">
<title>Valtiro Limited – Business Card</title>
<link rel="stylesheet" href="https://fonts.googleapis.com/css2?family=Arimo:wght@400;700&display=swap">
<style>
  :root {
    --page: #ffffff;
    --card: #ffffff;
    --frame: #9a9a9a;
    --ink: #111111;
    --brand-dark: #2b2b2b;
    --brand-blue: #2f6a8c;
  }
  * { margin: 0; padding: 0; box-sizing: border-box; }
  html, body {
    width: 1200px; height: 900px; overflow: hidden;
    background: var(--page);
    font-family: "Arimo", Arial, sans-serif;
    color: var(--ink);
  }
  .card {
    position: absolute;
    left: 236px; width: 728px; height: 429px;
    background: var(--card);
    border: 2px solid var(--frame);
  }
  .card--front { top: 15px; }
  .card--back { top: 455px; }

  .brand {
    position: absolute; left: 294px; top: 258px;
    display: flex; align-items: center; gap: 18px;
  }
  .brand__dot {
    width: 66px; height: 66px; border-radius: 50%;
    background: var(--brand-blue);
  }
  .brand__name {
    font-size: 70px; font-weight: 400; line-height: 1;
    color: var(--brand-dark); letter-spacing: 0.5px;
  }

  .person { position: absolute; left: 132px; top: 152px; }
  .person__name { font-size: 19px; font-weight: 700; color: var(--brand-blue); line-height: 25px; }
  .person__title { font-size: 19px; font-weight: 700; line-height: 25px; }

  .contact, .address {
    position: absolute; font-size: 19px; line-height: 25px;
  }
  .contact { left: 132px; top: 249px; }
  .address { left: 402px; top: 245px; }
  .address__company { font-size: 24px; font-weight: 700; line-height: 28px; }
</style>
</head>
<body>
  <section class="card card--front">
    <div class="brand">
      <span class="brand__dot"></span>
      <span class="brand__name">Valtiro</span>
    </div>
  </section>

  <section class="card card--back">
    <div class="person">
      <p class="person__name">Leon Fairholt</p>
      <p class="person__title">CEO</p>
    </div>
    <div class="contact">
      <p>leon@valtiro.co</p>
      <p>Ph: 0800 519 308</p>
      <p>Mob: +64 21 948 216</p>
      <p>www.valtiro.co</p>
    </div>
    <div class="address">
      <p class="address__company">Valtiro Limited</p>
      <p>Level 3, 42 Kestle St</p>
      <p>P O Box 462</p>
      <p>Paraparaumu 5391</p>
    </div>
  </section>
</body>
</html>
```